Business card design needed

A laid back coffee shop that has a great feel, that becomes a bar and grill at night. We are also wanting to cater for functions etc.
The business itself is painted dark blue/charcoal and has red doors.
Would like a logo that will be recognised when seen.

Industry/Entity Type

Coffee Shop

Contact Information for Business Card

The Lantern Coffee Bar & Grill
14b Wattle Rd
Kelmora NSW 2318
Ph. 02 4817 3362

Logo Text

Logo styles of interest
Emblem Logo
Abstract Logo
Wordmark Logo
Requirements
Must have
• A loyalty card on the back with 2 rows of 7 stamp spaces and a place to write a name and phone number (for a draw)

```html
<!DOCTYPE html>
<html lang="en">
<head>
<meta charset="utf-8">
<title>The Lantern Coffee Bar &amp; Grill – Business &amp; Loyalty Cards</title>
<link href="https://fonts.googleapis.com/css2?family=Montserrat:wght@300;400;600;700&display=swap" rel="stylesheet">
<style>
  :root {
    --page: #ffffff;
    --blue-light: #0aa0dc;
    --blue-dark: #0a6e9c;
    --grey-light: #b4b5b7;
    --grey-dark: #6a6b6d;
    --band-blue: rgba(0, 60, 100, 0.28);
    --band-grey: rgba(40, 40, 40, 0.22);
    --red: #e21d25;
    --white: #ffffff;
    --stamp-blue: rgba(190, 230, 250, 0.72);
    --stamp-grey: rgba(235, 236, 238, 0.8);
    --label-blue: #0a3d5c;
    --label-grey: #2e2e30;
  }
  * { box-sizing: border-box; margin: 0; padding: 0; }
  html, body { width: 1017px; height: 1200px; overflow: hidden; background: var(--page); }
  body { position: relative; font-family: "Montserrat", sans-serif; }

  .card {
    position: absolute;
    box-shadow: 0 8px 10px -4px rgba(0,0,0,0.28);
    overflow: hidden;
    color: var(--white);
  }
  .card--front { width: 518px; height: 304px; left: 18px; }
  .card--back { width: 300px; height: 518px; left: 669px; }
  .card--blue { background: radial-gradient(ellipse at 45% 40%, var(--blue-light) 0%, #0890c9 55%, var(--blue-dark) 100%); }
  .card--grey { background: radial-gradient(ellipse at 45% 35%, #d2d3d5 0%, var(--grey-light) 45%, var(--grey-dark) 100%); }

  .front-1 { top: 85px; }
  .front-2 { top: 719px; }
  .back-1 { top: 10px; }
  .back-2 { top: 644px; }

  /* Front */
  .brand {
    position: absolute; left: 0; right: 0; top: 92px;
    display: flex; align-items: center; justify-content: center; gap: 14px;
  }
  .brand__dot { width: 30px; height: 30px; border-radius: 50%; background: var(--red); flex: none; }
  .brand__name {
    font-weight: 700; font-size: 40px; letter-spacing: 1px; color: var(--white);
    text-transform: uppercase; line-height: 1;
  }
  .tagline {
    position: absolute; left: 0; right: 0; top: 220px; text-align: center;
    font-weight: 600; font-size: 16px; letter-spacing: 0.5px;
  }
  .address-band {
    position: absolute; left: 0; right: 0; bottom: 0; height: 36px;
    display: flex; align-items: center; justify-content: center;
    font-weight: 400; font-size: 15px; letter-spacing: 0.2px;
  }
  .card--blue .address-band { background: var(--band-blue); }
  .card--grey .address-band { background: var(--band-grey); }

  /* Back */
  .mini-brand { position: absolute; left: 0; right: 0; top: 28px; text-align: center; }
  .mini-brand__name {
    display: inline-flex; align-items: center; gap: 6px;
    font-weight: 700; font-size: 17px; letter-spacing: 0.5px; text-transform: uppercase;
  }
  .mini-brand__dot { width: 11px; height: 11px; border-radius: 50%; background: var(--red); }
  .mini-brand__tag { display: block; font-size: 6px; font-weight: 600; margin-top: 5px; letter-spacing: 0.3px; }

  .stamps {
    position: absolute; left: 23px; top: 200px;
    display: grid; grid-template-columns: repeat(7, 32px); grid-auto-rows: 44px;
    column-gap: 5px; row-gap: 10px;
  }
  .stamp { border-radius: 6px; }
  .card--blue .stamp { background: var(--stamp-blue); }
  .card--grey .stamp { background: var(--stamp-grey); }

  .field-label {
    position: absolute; left: 20px; font-weight: 300; font-size: 17px; line-height: 1;
  }
  .card--blue .field-label { color: var(--label-blue); }
  .card--grey .field-label { color: var(--label-grey); }
  .field-label--name { top: 410px; }
  .field-label--phone { top: 460px; }
  .field {
    position: absolute; left: 20px; width: 257px; height: 25px; background: var(--white);
  }
  .field--name { top: 430px; }
  .field--phone { top: 479px; }
</style>
</head>
<body>

  <section class="card card--front card--blue front-1">
    <div class="brand"><span class="brand__dot"></span><span class="brand__name">The Lantern</span></div>
    <p class="tagline">COFFEE BAR &amp; GRILL</p>
    <p class="address-band">14b Wattle Rd Kelmora NSW 2318 Ph. 02 4817 3362</p>
  </section>

  <section class="card card--back card--blue back-1">
    <div class="mini-brand">
      <span class="mini-brand__name"><span class="mini-brand__dot"></span>The Lantern</span>
      <span class="mini-brand__tag">COFFEE BAR &amp; GRILL</span>
    </div>
    <div class="stamps">
      <div class="stamp"></div><div class="stamp"></div><div class="stamp"></div><div class="stamp"></div><div class="stamp"></div><div class="stamp"></div><div class="stamp"></div>
      <div class="stamp"></div><div class="stamp"></div><div class="stamp"></div><div class="stamp"></div><div class="stamp"></div><div class="stamp"></div><div class="stamp"></div>
    </div>
    <p class="field-label field-label--name">NAME</p>
    <div class="field field--name"></div>
    <p class="field-label field-label--phone">PHONE</p>
    <div class="field field--phone"></div>
  </section>

  <section class="card card--front card--grey front-2">
    <div class="brand"><span class="brand__dot"></span><span class="brand__name">The Lantern</span></div>
    <p class="tagline">COFFEE BAR &amp; GRILL</p>
    <p class="address-band">14b Wattle Rd Kelmora NSW 2318 Ph. 02 4817 3362</p>
  </section>

  <section class="card card--back card--grey back-2">
    <div class="mini-brand">
      <span class="mini-brand__name"><span class="mini-brand__dot"></span>The Lantern</span>
      <span class="mini-brand__tag">COFFEE BAR &amp; GRILL</span>
    </div>
    <div class="stamps">
      <div class="stamp"></div><div class="stamp"></div><div class="stamp"></div><div class="stamp"></div><div class="stamp"></div><div class="stamp"></div><div class="stamp"></div>
      <div class="stamp"></div><div class="stamp"></div><div class="stamp"></div><div class="stamp"></div><div class="stamp"></div><div class="stamp"></div><div class="stamp"></div>
    </div>
    <p class="field-label field-label--name">NAME</p>
    <div class="field field--name"></div>
    <p class="field-label field-label--phone">PHONE</p>
    <div class="field field--phone"></div>
  </section>

</body>
</html>
```